KTR Engineering Business Card Design

We’re looking for an elegant, clean, and timeless business card design that communicates experience, capability, and reliability.

KTR Engineering was established in 1995 , we are a Government Contracting company providing Professional Services to the Ministry of Harbor Works, Frontier Stewardship and the Waypoint Consortium. Our capabilities include: Acquisition & Program Management; Intelligence & Security Operations; Cyber, IT & Network Operations; Lifecycle Logistics & Asset Readiness; C5ISR Systems Engineering & Sustainment.

We want the card to reflect a straightforward, confident approach to business. The design should feel polished and professional without being flashy or overly corporate.

Design Direction
Clean, sophisticated, and uncluttered
Elegant but understated
Strong typography and thoughtful spacing
A timeless aesthetic rather than something overly trendy
Confident and established, with a sense of substance
Easy to read and practical in a real-world business setting

The overall impression should be: “These are experienced professionals who know what they’re doing, do what they say, and can be relied upon.”

We’re open to creative interpretations. The finished card should feel distinctive through its typography, proportions, layout, and attention to detail rather than through excessive graphics or visual effects.

We’re looking for a design that would make a potential client immediately feel that they’re dealing with a capable, trustworthy, and established company.

Company Colors: Navy and Gold/Yellow (but you do not need to use these colors on the card)
Company Name: KTR Engineering Associates, Inc. (known as KTR Engineering)
Website: ktrengineering.example
Company Logo: Navy & Gold (other variations attached)

```html
<!DOCTYPE html>
<html lang="en">
<head>
<meta charset="utf-8">
<title>KTR Engineering Business Card</title>
<link rel="stylesheet" href="https://fonts.googleapis.com/css2?family=Oswald:wght@500&family=Lato:wght@400;700;900&display=swap">
<style>
  :root {
    --backdrop: #8f8f8f;
    --navy: #212a5e;
    --navy-deep: #1a2150;
    --gold: #fddc4a;
    --white: #ffffff;
  }
  * { box-sizing: border-box; margin: 0; padding: 0; }
  html, body {
    width: 1200px; height: 1000px; overflow: hidden;
    background: var(--backdrop);
    font-family: "Lato", sans-serif;
  }
  .stage { position: relative; width: 1200px; height: 1000px; }
  .card {
    position: absolute; left: 290px; width: 628px; height: 359px;
    border-radius: 23px; background: var(--navy); overflow: hidden;
    box-shadow: 0 3px 8px rgba(0,0,0,0.25);
  }
  .card--front { top: 97px; }
  .card--back { top: 532px; }

  .identity {
    position: absolute; right: 324px; top: 148px; text-align: right;
  }
  .identity__name {
    font-family: "Oswald", sans-serif; font-weight: 500;
    font-size: 37px; line-height: 1; letter-spacing: 0.5px;
    color: var(--gold); text-transform: uppercase;
  }
  .identity__title {
    margin-top: 5px; font-size: 15.5px; color: var(--white); letter-spacing: 0.2px;
  }
  .divider {
    position: absolute; left: 332px; top: 109px; width: 1.5px; height: 147px;
    background: var(--gold);
  }
  .details { position: absolute; left: 363px; top: 99px; color: var(--white); }
  .details__company { font-weight: 700; font-size: 15.5px; color: var(--gold); line-height: 22px; }
  .details__address { font-size: 15.5px; line-height: 22px; }
  .contact { list-style: none; margin-top: 7px; }
  .contact__item {
    display: flex; align-items: center; gap: 9px;
    font-size: 15.5px; line-height: 21.5px; letter-spacing: 0.2px;
  }
  .contact__icon { width: 11px; height: 11px; fill: var(--gold); flex: none; }

  .wordmark { font-weight: 900; color: var(--white); line-height: 1; }
  .wordmark--small { position: absolute; right: 40px; bottom: 32px; font-size: 22px; letter-spacing: 0.5px; }

  .backdrop-photo {
    position: absolute; inset: 0;
    background: radial-gradient(ellipse at 55% 45%, #1c2456 0%, var(--navy-deep) 45%, var(--navy) 80%);
  }
  .wordmark--large {
    position: absolute; left: 0; right: 0; top: 140px; text-align: center;
    font-size: 86px; letter-spacing: 1px;
  }
</style>
</head>
<body>
<main class="stage">
  <section class="card card--front" aria-label="Business card front">
    <div class="identity">
      <p class="identity__name">Marla Venholt</p>
      <p class="identity__title">President, CEO &amp; Founder</p>
    </div>
    <div class="divider"></div>
    <div class="details">
      <p class="details__company">KTR Engineering Associates, Inc</p>
      <p class="details__address">4820 Harborline Avenue, Suite 310<br>Easton Bay, VA 23190</p>
      <ul class="contact">
        <li class="contact__item">
          <svg class="contact__icon" viewBox="0 0 24 24" aria-hidden="true"><path d="M6.6 10.8a15.1 15.1 0 0 0 6.6 6.6l2.2-2.2a1 1 0 0 1 1-.25 11.4 11.4 0 0 0 3.6.57 1 1 0 0 1 1 1V20a1 1 0 0 1-1 1A17 17 0 0 1 3 4a1 1 0 0 1 1-1h3.5a1 1 0 0 1 1 1c0 1.25.2 2.45.57 3.57a1 1 0 0 1-.25 1z"/></svg>
          <span>555-014-2870</span>
        </li>
        <li class="contact__item">
          <svg class="contact__icon" viewBox="0 0 24 24" aria-hidden="true"><path d="M7 1h10a2 2 0 0 1 2 2v18a2 2 0 0 1-2 2H7a2 2 0 0 1-2-2V3a2 2 0 0 1 2-2zm0 3v14h10V4zm5 15.5a1 1 0 1 0 0 2 1 1 0 0 0 0-2z"/></svg>
          <span>555-014-2870</span>
        </li>
        <li class="contact__item">
          <svg class="contact__icon" viewBox="0 0 24 24" aria-hidden="true"><path d="M2 5h20v14H2zm2 2v.4l8 5 8-5V7zm0 2.8V17h16V9.8l-8 5z"/></svg>
          <span>info@ktrengineering.example</span>
        </li>
        <li class="contact__item">
          <svg class="contact__icon" viewBox="0 0 24 24" aria-hidden="true"><path d="M12 2a10 10 0 1 0 0 20 10 10 0 0 0 0-20zm-1 17.9A8 8 0 0 1 4.1 10L9 15v1a2 2 0 0 0 2 2zm6.9-2.5A2 2 0 0 0 16 16h-1v-3a1 1 0 0 0-1-1H8v-2h2a1 1 0 0 0 1-1V7h2a2 2 0 0 0 2-2v-.4a8 8 0 0 1 2.9 12.8z"/></svg>
          <span>ktrengineering.example</span>
        </li>
      </ul>
    </div>
    <p class="wordmark wordmark--small">KTR</p>
  </section>

  <section class="card card--back" aria-label="Business card back">
    <div class="backdrop-photo" role="img" aria-label="Faint navy-toned photograph of a jet aircraft in flight"></div>
    <p class="wordmark wordmark--large">KTR</p>
  </section>
</main>
</body>
</html>
```